Harbor Compass - Book Cover

I need a book cover for my debut work, "Harbor Compass - Turning the Tide, One Step at a Time." While the website isn't complete, you can get a sense of what I am writing about by looking at my website, harborcompassbooks.org. The book is a leadership development book, but more of a personal change journey. The emphasis is on figuring out how to combine you work, social, and own self into an authentic package that not only resonates with others, but makes what you achieve more fulfilling.

I am attaching a copy of my logo so you can get a sense of what I like. I would prefer to not have the cover be photographic, but am open to suggestions. This will be a series of books so maintaining some sense of style will be important, and can garner future work.

Industry/Entity Type

Leadership

```html
<!DOCTYPE html>
<html lang="en">
<head>
<meta charset="utf-8">
<title>Harbor Compass – Book Cover</title>
<link rel="stylesheet" href="https://fonts.googleapis.com/css2?family=Source+Sans+3:wght@300;400;600&display=swap">
<style>
  :root {
    --page-bg: #f4f4f4;
    --page-edge: #e6e6e6;
    --cover-green: #9ab53d;
    --cover-green-light: #bdd07a;
    --cover-black: #232323;
    --divider-white: #ffffff;
    --title-white: #ffffff;
    --ink-dark: #1f2a10;
    --mark-grey: #6b6b6b;
  }
  * { margin: 0; padding: 0; box-sizing: border-box; }
  html, body {
    width: 1200px;
    height: 1000px;
    overflow: hidden;
  }
  body {
    background: radial-gradient(ellipse at center, #ffffff 0%, var(--page-bg) 55%, var(--page-edge) 100%);
    font-family: "Source Sans 3", "Helvetica Neue", Arial, sans-serif;
    position: relative;
  }
  .book-cover {
    position: absolute;
    left: 355px;
    top: 110px;
    width: 490px;
    height: 760px;
    background: var(--cover-black);
    overflow: hidden;
    box-shadow: 0 18px 40px rgba(0,0,0,0.18);
  }
  .cover-top {
    position: absolute;
    inset: 0 0 auto 0;
    height: 468px;
    background: linear-gradient(200deg, var(--cover-green-light) 0%, var(--cover-green) 32%, var(--cover-green) 100%);
    border-bottom: 9px solid var(--divider-white);
  }
  .cover-text {
    position: absolute;
    left: 62px;
    top: 78px;
    right: 40px;
  }
  .author-name {
    font-size: 13px;
    font-weight: 400;
    letter-spacing: 0.06em;
    text-transform: uppercase;
    color: var(--ink-dark);
  }
  .book-title {
    margin-top: 16px;
    margin-left: 18px;
    font-size: 44px;
    font-weight: 300;
    line-height: 1.05;
    color: var(--title-white);
  }
  .book-subtitle {
    margin-top: 10px;
    margin-left: 40px;
    font-size: 24px;
    font-weight: 400;
    line-height: 1.2;
    color: var(--ink-dark);
  }
  .series-mark {
    position: absolute;
    right: 44px;
    bottom: 58px;
    display: flex;
    align-items: center;
    gap: 14px;
  }
  .series-dot {
    width: 34px;
    height: 34px;
    border-radius: 50%;
    background: var(--mark-grey);
  }
  .series-name {
    font-size: 30px;
    font-weight: 300;
    color: var(--title-white);
  }
</style>
</head>
<body>
  <main class="book-cover" aria-label="Harbor Compass book cover">
    <section class="cover-top">
      <div class="cover-text">
        <p class="author-name">Author's Name</p>
        <h1 class="book-title">Harbor Compass</h1>
        <p class="book-subtitle">Turning the Tide,<br>One Step at a Time.</p>
      </div>
    </section>
    <div class="series-mark">
      <span class="series-dot"></span>
      <span class="series-name">Harbor Compass</span>
    </div>
  </main>
</body>
</html>
```